Automotive eCommerce Business looking for a business card design

Looking for a clean and simple business card design. Our company name is "Tundra Motors" and we are a company specializing in the ecommerce sales of automotive parts, specifically for pick up trucks and large SUVs. Our company colours are red, black, and white.

Feel free to use the logo provided or create a new logo that you seem fit. Looking forward to your creative ideas!

Industry/Entity Type

Automotive

Contact Information for Business Card

We were thinking of a possibly two-sided design featuring just the logo and company name on one side, and personal information on the other side. Single sided designs will be considered as well.

Font styles to use
Serif
Sans Serif
Decorative

Colors
ec1f27
ffffff
000000

Requirements
Must have
• Space for employee's name, title, phone number and email address, along with the company address and website somewhere.

```html
<!DOCTYPE html>
<html lang="en">
<head>
<meta charset="utf-8">
<title>Tundra Motors – Business Card</title>
<link rel="stylesheet" href="https://fonts.googleapis.com/css2?family=Cinzel:wght@500&family=Comfortaa:wght@400;500&display=swap">
<style>
  :root {
    --brand-red: #ec1f27;
    --deep-red: #b3161d;
    --ink: #000000;
    --paper: #ffffff;
    --carbon-dark: #141414;
    --carbon-light: #2c2c2c;
    --silver: #c9c9c9;
    --backdrop: #d2d2d2;
  }
  * { margin: 0; padding: 0; box-sizing: border-box; }
  html, body {
    width: 742px;
    height: 1200px;
    overflow: hidden;
    background: var(--backdrop);
  }
  .sheet {
    position: relative;
    width: 742px;
    height: 1200px;
  }
  .card {
    position: absolute;
    left: 51px;
    width: 640px;
    height: 366px;
    overflow: hidden;
    box-shadow: 0 2px 6px rgba(0,0,0,0.18);
  }
  .card--front { top: 214px; }
  .card--back  { top: 620px; background: var(--ink); }

  .card__art { display: block; width: 100%; height: 100%; }
  .wordmark-front {
    font-family: "Cinzel", serif;
    font-weight: 500;
    font-size: 44px;
    letter-spacing: 5px;
    fill: var(--paper);
  }

  .back-glow {
    position: absolute;
    left: 300px;
    top: -40px;
    width: 420px;
    height: 450px;
    background: radial-gradient(ellipse at 50% 50%, rgba(200,32,38,0.85) 0%, rgba(140,20,26,0.55) 40%, rgba(0,0,0,0) 70%);
  }
  .back-content {
    position: absolute;
    left: 36px;
    top: 112px;
    font-family: "Comfortaa", sans-serif;
  }
  .wordmark-back {
    font-family: "Cinzel", serif;
    font-weight: 500;
    font-size: 15px;
    letter-spacing: 2px;
    color: var(--brand-red);
  }
  .person-name {
    margin-top: 22px;
    font-size: 25px;
    font-weight: 500;
    letter-spacing: 1.5px;
    color: var(--paper);
  }
  .person-title {
    margin-top: 4px;
    font-size: 15px;
    letter-spacing: 1.2px;
    color: var(--brand-red);
  }
  .contact-list {
    list-style: none;
    margin-top: 20px;
  }
  .contact-item {
    display: flex;
    align-items: center;
    height: 21px;
    font-size: 13px;
    letter-spacing: 1px;
    color: var(--paper);
  }
  .contact-icon {
    width: 17px;
    height: 17px;
    margin-right: 7px;
    border-radius: 3px;
    background: var(--brand-red);
    display: flex;
    align-items: center;
    justify-content: center;
    flex-shrink: 0;
  }
  .contact-icon svg { width: 11px; height: 11px; }
</style>
</head>
<body>
<main class="sheet">

  <section class="card card--front" aria-label="Card front">
    <svg class="card__art" viewBox="0 0 640 366" xmlns="http://www.w3.org/2000/svg">
      <defs>
        <linearGradient id="carbonTone" x1="0" y1="0" x2="1" y2="1">
          <stop offset="0" stop-color="#2e2e2e"/>
          <stop offset="0.5" stop-color="#1c1c1c"/>
          <stop offset="1" stop-color="#101010"/>
        </linearGradient>
      </defs>
      <rect width="640" height="366" fill="url(#carbonTone)" role="img" aria-label="Carbon fibre texture panel"/>
      <polygon class="divider-stripe" points="493,0 507,0 340,366 326,366" fill="var(--silver)"/>
      <polygon class="red-panel" points="0,0 493,0 326,366 0,366" fill="var(--brand-red)"/>
      <text class="wordmark-front" x="342" y="316" text-anchor="end">TUNDRA</text>
      <text class="wordmark-front" x="378" y="316" text-anchor="start">MOTORS</text>
    </svg>
  </section>

  <section class="card card--back" aria-label="Card back">
    <div class="back-glow" aria-hidden="true"></div>
    <div class="back-content">
      <p class="wordmark-back">TUNDRA MOTORS</p>
      <p class="person-name">Mara Holt</p>
      <p class="person-title">Product Development Manager</p>
      <ul class="contact-list">
        <li class="contact-item">
          <span class="contact-icon">
            <svg viewBox="0 0 12 12"><circle cx="6" cy="6" r="2" fill="none" stroke="#fff" stroke-width="1.3"/><path d="M8 4v3a1.2 1.2 0 0 0 2.4 0V6A4.4 4.4 0 1 0 8 9.8" fill="none" stroke="#fff" stroke-width="1.3"/></svg>
          </span>
          mara@tundramotors.com
        </li>
        <li class="contact-item">
          <span class="contact-icon">
            <svg viewBox="0 0 12 12"><path d="M4 1.5 L5.5 1.5 L6 4 L4.8 4.8 Q5.6 7 7.2 7.8 L8 6.6 L10.5 7.1 L10.5 8.6 Q10 10.5 8 10.3 Q2 9.4 1.7 3.6 Q1.8 1.7 4 1.5Z" fill="#fff"/></svg>
          </span>
          1 (888) 555-0142
        </li>
        <li class="contact-item">
          <span class="contact-icon">
            <svg viewBox="0 0 12 12"><g fill="none" stroke="#fff" stroke-width="1"><circle cx="6" cy="6" r="4.5"/><ellipse cx="6" cy="6" rx="2" ry="4.5"/><path d="M1.5 6h9M2.3 3.6h7.4M2.3 8.4h7.4"/></g></svg>
          </span>
          www.tundramotors.com
        </li>
      </ul>
    </div>
  </section>

</main>
</body>
</html>
```